Company or website name
- Dr. Renaud Vasquelle
- Links to the website
- Retired doctor; professional speaker, Life coach, author, healthcare consultant
- Other Facts

```html
<!DOCTYPE html>
<html lang="en">
<head>
<meta charset="utf-8">
<title>Vasquelle Coaching and Consulting</title>
<link href="https://fonts.googleapis.com/css2?family=Roboto:wght@500;700&family=Arimo:wght@400;700&display=swap" rel="stylesheet">
<style>
:root{
  --bg:#f1f1f1;
  --page:#ffffff;
  --ink:#333333;
  --brand:#1d5d86;
  --nav:#8a8a8a;
  --btn:#333333;
  --strip:#f4f4f4;
  --muted:#999999;
}
*{box-sizing:border-box;margin:0;padding:0}
html,body{width:710px;height:1200px;overflow:hidden;background:var(--bg);font-family:"Arimo",Arial,sans-serif;color:var(--ink)}
.page{position:absolute;left:21px;top:0;width:668px;height:1166px;background:var(--page);box-shadow:0 0 3px rgba(0,0,0,.2)}
.header{position:absolute;left:0;top:0;width:100%;height:70px}
.logo{position:absolute;left:7px;top:24px;display:flex;align-items:center;gap:8px}
.logo-name{font-family:"Roboto",sans-serif;font-weight:700;font-size:19px;color:var(--brand);line-height:1}
.logo-sub{font-size:7.5px;color:var(--brand);margin-top:2px;margin-left:2px}
.logo-dot{width:22px;height:22px;border-radius:50%;border:2px solid var(--brand)}
.nav{position:absolute;right:7px;top:33px;display:flex;gap:21px}
.nav a{font-family:"Roboto",sans-serif;font-weight:700;font-size:13.5px;color:var(--nav);text-decoration:none}
.hero{position:absolute;left:0;top:70px;width:100%;height:375px;background:
  radial-gradient(ellipse at 10% 40%,#6a3a8a 0,transparent 35%),
  radial-gradient(ellipse at 90% 25%,#8a5a20 0,transparent 35%),
  radial-gradient(ellipse at 85% 70%,#4a1f55 0,transparent 40%),
  radial-gradient(ellipse at 30% 80%,#9a6a6a 0,transparent 40%),
  linear-gradient(90deg,#4a2a4a,#7a5a50 40%,#6a4a30 70%,#3a1a40)}
.video{position:absolute;left:167px;top:14px;width:334px;height:250px;border:1px solid #aaa;background:rgba(255,255,255,.25);padding:6px}
.video-photo{width:100%;height:100%;background:radial-gradient(ellipse at 55% 45%,#c8b8a8 0,#8a7f78 35%,#3a3a3a 75%,#1a1a1a)}
.play{position:absolute;left:14px;top:12px;display:flex;align-items:center;gap:5px;font-family:"Roboto",sans-serif;font-weight:700;font-size:13px;color:#fff}
.hero h1{position:absolute;left:0;width:100%;top:275px;text-align:center;font-family:"Roboto",sans-serif;font-weight:700;font-size:17.5px;color:#fff;text-shadow:0 1px 2px rgba(0,0,0,.5)}
.hero p{position:absolute;left:180px;width:308px;top:311px;text-align:center;font-size:9px;line-height:11.8px;color:#fff;text-shadow:0 1px 1px rgba(0,0,0,.4)}
.feature{position:absolute;width:150px}
.feature .icon{display:block;margin:0 auto;width:42px;height:42px}
.feature h2{text-align:center;font-family:"Roboto",sans-serif;font-weight:700;font-size:12px;margin-top:18px;margin-left:-30px;margin-right:-30px}
.feature p{font-size:10.4px;line-height:11.8px;margin-top:11px;letter-spacing:.1px}
.more{display:inline-block;background:var(--btn);color:#fff;font-size:10.4px;padding:0 4px;margin-top:2px;line-height:13px;text-decoration:none}
.shelf{position:absolute;left:0;top:1051px;width:100%;height:115px;background:var(--strip)}
.book{position:absolute;top:0;width:85px}
.cover{width:70px;height:70px}
.book a{display:block;margin-top:5px;font-size:7.5px;line-height:9px;color:var(--ink)}
.next{width:28px;height:70px;background:linear-gradient(#3fa83a,#1d7a1a);display:flex;align-items:center;justify-content:center}
.footer{position:absolute;left:0;width:710px;top:1178px;text-align:center;font-size:7.5px;color:var(--muted)}
</style>
</head>
<body>
<div class="page">
  <header class="header">
    <div class="logo">
      <div>
        <div class="logo-name">Vasquelle</div>
        <div class="logo-sub">Coaching and Consulting</div>
      </div>
      <span class="logo-dot"></span>
    </div>
    <nav class="nav"><a href="#">Home</a><a href="#">About</a><a href="#">Booking</a><a href="#">Contact</a></nav>
  </header>

  <section class="hero" role="img" aria-label="Softly blurred purple and amber lights">
    <div class="video">
      <div class="video-photo" role="img" aria-label="Portrait of Dr. Renaud Vasquelle"></div>
      <div class="play"><svg width="12" height="12" viewBox="0 0 12 12"><circle cx="6" cy="6" r="5" fill="none" stroke="#fff" stroke-width="1.4"/><path d="M5 3.6v4.8L8.4 6z" fill="#fff"/></svg>Play Video</div>
    </div>
    <h1>My Personal Purpose Statement</h1>
    <p>I hereby pledge my life to my greatest expression of love and service for the benefit of all humanity. I accomplish this by helping people tap into their potential, using the written and spoken word; empowering ordinary people into exceptional life-fulfilled individuals</p>
  </section>

  <div class="feature" style="left:50px;top:487px">
    <svg class="icon" viewBox="0 0 42 42"><path d="M21 2l6 3h6l3 6 3 6-2 6 2 6-3 6-6 3-6 3-6-3-6-3-3-6-3-6 2-6-2-6 3-6 3-3 6-3z" fill="none" stroke="#333" stroke-width="2"/><circle cx="21" cy="22" r="10" fill="none" stroke="#333" stroke-width="2"/><path d="M21 22v-6M21 22h5M19 10h4" stroke="#333" stroke-width="2"/></svg>
    <h2>1-Minute Motivator</h2>
    <p>Over the last number of years, the 1-Minute Motivator e-zine has inspired and motivated its readers with various insights from Dr. Renaud Vasquelle. The e-zine is no longer active, but listed below are the previous editions for your reading pleasure.</p>
    <a class="more" href="#">More →</a>
  </div>
  <div class="feature" style="left:259px;top:487px">
    <svg class="icon" viewBox="0 0 42 42"><path d="M21 2l6 3h6l3 6 3 6-2 6 2 6-3 6-6 3-6 3-6-3-6-3-3-6-3-6 2-6-2-6 3-6 3-3 6-3z" fill="none" stroke="#333" stroke-width="2"/><path d="M20 9v26" stroke="#333" stroke-width="2.4"/><path d="M21 13h9l3 3-3 3h-9zM19 20h-8l-3 3 3 3h8z" fill="#333"/></svg>
    <h2>Words Of Wisdom</h2>
    <p>This is the beginning of a new day for you - A new era. You will understand that every day is given to you to do as you will. You can waste it or use it for good. What you do is important because you are exchanging a day of your life for it. When tomorrow comes, this will be gone forever and in its place is something that you have left behind - Let it be something great!</p>
    <a class="more" href="#">More →</a>
  </div>
  <div class="feature" style="left:468px;top:487px">
    <svg class="icon" viewBox="0 0 42 42"><path d="M21 2l6 3h6l3 6 3 6-2 6 2 6-3 6-6 3-6 3-6-3-6-3-3-6-3-6 2-6-2-6 3-6 3-3 6-3z" fill="none" stroke="#333" stroke-width="2"/><circle cx="21" cy="21" r="12" fill="#333"/><rect x="14" y="16" width="14" height="4" fill="#fff"/><rect x="15" y="21" width="12" height="7" fill="#fff"/><rect x="18" y="23" width="6" height="2" fill="#333"/></svg>
    <h2>Available Seminar Topics</h2>
    <p>All of our presentations are tailored to meet the individual needs of our clients, and are developed after careful discussion with meeting planners.</p>
    <a class="more" href="#">More →</a>
  </div>

  <div class="feature" style="left:50px;top:780px">
    <svg class="icon" viewBox="0 0 42 42"><path d="M21 2l6 3h6l3 6 3 6-2 6 2 6-3 6-6 3-6 3-6-3-6-3-3-6-3-6 2-6-2-6 3-6 3-3 6-3z" fill="none" stroke="#333" stroke-width="2"/><path d="M9 13l8-3 8 3 8-3v19l-8 3-8-3-8 3z" fill="none" stroke="#333" stroke-width="2" stroke-linejoin="round"/><path d="M17 10v19M25 13v19" stroke="#333" stroke-width="2"/></svg>
    <h2>Creat Your Perfect Life</h2>
    <p>In the Perfect Life Program, you identify the 25 elements of your perfect life. These elements typically include several of each of the following types of items</p>
    <a class="more" href="#">More →</a>
  </div>
  <div class="feature" style="left:259px;top:780px">
    <svg class="icon" viewBox="0 0 42 42"><path d="M21 2l6 3h6l3 6 3 6-2 6 2 6-3 6-6 3-6 3-6-3-6-3-3-6-3-6 2-6-2-6 3-6 3-3 6-3z" fill="none" stroke="#333" stroke-width="2"/><path d="M17 11h15v11h-4v4l-4-4h-7z" fill="#333"/><path d="M10 18h11v10h-6l-4 4v-4h-1z" fill="#333" stroke="#fff" stroke-width="1.5"/></svg>
    <h2>Want Coaching?</h2>
    <p>Almost all of us can benefit from hiring a coach, provided we are prepared to make changes. Regardless of whether you hire a coach to help you with your career, your relationships, or your personal and spiritual development, here are some hints towards making the best use of your coach.</p>
    <a class="more" href="#">More →</a>
  </div>
  <div class="feature" style="left:468px;top:780px">
    <svg class="icon" viewBox="0 0 42 42"><path d="M21 2l6 3h6l3 6 3 6-2 6 2 6-3 6-6 3-6 3-6-3-6-3-3-6-3-6 2-6-2-6 3-6 3-3 6-3z" fill="none" stroke="#333" stroke-width="2"/><circle cx="16" cy="16" r="4.5" fill="#333"/><path d="M8 31c0-7 3-10 8-10s8 3 8 10z" fill="#333"/><circle cx="26" cy="17" r="4.5" fill="#333" stroke="#fff" stroke-width="1.2"/><path d="M18 33c0-7 3-11 8-11s8 4 8 11z" fill="#333" stroke="#fff" stroke-width="1.2"/></svg>
    <h2>Booking Renaud</h2>
    <p>For those interested in having Renaud speak at their next event, please review and fill-out the forms, which will help Renaud to tailor his message to meet your group's needs.</p>
    <a class="more" href="#">More →</a>
  </div>

  <section class="shelf">
    <div class="book" style="left:7px;top:14px"><div class="cover" role="img" aria-label="Book cover, Boiling Point Plus" style="background:linear-gradient(135deg,#5a6aa0,#1a2040)"></div><a href="#">Boiling Point Plus</a></div>
    <div class="book" style="left:132px;top:14px"><div class="cover" role="img" aria-label="Book cover, The Heart of Leading" style="background:linear-gradient(160deg,#7a4a2a,#c8a070 60%,#e8dcc0)"></div><a href="#">The Heart of Leading</a></div>
    <div class="book" style="left:257px;top:14px"><div class="cover" role="img" aria-label="Book cover, Little Ones, Big Hours" style="background:linear-gradient(#d8d0c0,#8a7a60)"></div><a href="#">Little Ones, Big Hours</a></div>
    <div class="book" style="left:383px;top:14px"><div class="cover" role="img" aria-label="Book cover, The Lift of Outlook" style="background:linear-gradient(135deg,#1a4a8a,#5a8ac0 50%,#1a2a50)"></div><a href="#">The Lift of Outlook</a></div>
    <div class="book" style="left:508px;top:14px"><div class="cover" role="img" aria-label="Book cover, Ten Steps Toward Success" style="background:linear-gradient(#8a8a5a,#6a6a40)"></div><a href="#">Ten Steps Toward Success</a></div>
    <div class="book" style="left:633px;top:14px;width:28px"><div class="next"><svg width="12" height="16" viewBox="0 0 12 16"><path d="M1 1l10 7-10 7z" fill="#fff"/></svg></div><a href="#" style="text-align:right">more</a></div>
  </section>
</div>
<div class="footer">©2013 Dr. Renaud A. Vasquelle</div>
</body>
</html>
```